Innovative IT Service Provider seeks engaging overview presentation to capture new business

*Please see attached Creative Brief for full details*

Overall Goals
The goal of this presentation is to provide new, prospective clients with an introduction to Harborline Systems, the services we provide, and what makes us a unique and superior choice for their IT Services. The deck should be able to clearly relay this information while clients review it on their own, without further explanation from a company representative.

Design Goals
We are looking for a professional, modern, streamlined, sleek design that reflects our status as a leader in information technology and innovation.

Company Overview
As an IT Managed Service Provider, companies choose to outsource some or all of their internal IT functions to us to take advantage of our many areas of expertise and so they can focus on their core business, whatever industry they may be in. We also specialize in IT Cyber Security and Consulting, always providing our clients with thought leadership and insight into the latest IT innovations. We ultimately find ways to deliver value to our clients through our various IT solutions.

```html
<!DOCTYPE html>
<html lang="en">
<head>
<meta charset="utf-8">
<title>Harborline Systems – Overview Deck</title>
<link href="https://fonts.googleapis.com/css2?family=Roboto:wght@300;400;500;700&display=swap" rel="stylesheet">
<style>
:root{
  --canvas:#e4e5e8;
  --navy:#14386b;
  --blue:#1565b4;
  --blue-mid:#1f7fd0;
  --sky:#36ade6;
  --title:#2b98de;
  --red:#c41f2e;
  --grey:#8f9194;
  --grey-band:#9a9c9f;
  --text:#2a2d33;
  --green:#1f7a3a;
  --white:#fff;
}
*{box-sizing:border-box;margin:0;padding:0}
html,body{width:1200px;height:950px;overflow:hidden}
body{background:var(--canvas);font-family:"Roboto",Arial,sans-serif;color:var(--text);position:relative}
.slide{position:absolute;width:366px;height:206px;overflow:hidden;background:var(--white)}
.abs{position:absolute}
.blue-bg{background:linear-gradient(135deg,#1b4f93 0%,#1766b8 50%,#1c7fd0 100%);color:var(--white)}
.photo{position:absolute}
/* shared white-slide parts */
.s-title{position:absolute;left:22px;top:12px;font-size:10px;font-weight:300;color:var(--title)}
.s-rule{position:absolute;left:22px;top:28px;width:20px;height:1.5px;background:var(--red)}
.footer-bar{position:absolute;left:0;bottom:2px;width:100%;height:4px}
.footer-bar .g{position:absolute;left:0;top:1px;height:3px;width:260px;background:var(--grey)}
.footer-bar .b{position:absolute;right:0;top:0;height:4px;width:108px;background:var(--sky);clip-path:polygon(4px 0,100% 0,100% 100%,0 100%)}
.footer-bar .n{position:absolute;right:4px;top:-1px;font-size:4px;color:#fff}
.small-h{font-size:5.6px;font-weight:700;color:var(--text)}
.bullets{list-style:none}
.bullets li{position:relative;padding-left:9px;font-size:5.6px;line-height:10.6px}
.bullets li::before{content:"";position:absolute;left:1px;top:4.5px;width:1.6px;height:1.6px;border-radius:50%;background:currentColor}
.logo{position:absolute;display:flex;align-items:center;gap:5px}
.logo .mark{width:22px;height:22px;background:var(--navy)}
.logo .name{font-size:8px;font-weight:500;letter-spacing:1px;color:var(--navy);line-height:9px}
.logo .name small{display:block;font-size:5px;letter-spacing:.8px;padding-left:9px}
</style>
</head>
<body>

<!-- 1 Welcome -->
<section class="slide welcome" style="left:35px;top:37px">
  <div class="abs" style="left:0;top:42px;width:366px;height:118px;background:var(--red);clip-path:polygon(0 0,100% 0,100% 100%,145px 100%,0 100%)"></div>
  <div class="abs" style="left:0;top:45px;width:366px;height:124px;background:var(--sky);clip-path:polygon(150px 0,100% 0,100% 100%,157px 100%,150px 96%)"></div>
  <div class="photo" role="img" aria-label="Hand touching a tablet with floating security and network icons" style="left:0;top:39px;width:366px;height:114px;background:linear-gradient(90deg,#0e2a4f 0%,#1a4d86 38%,#1f6cb8 62%,#1b7acd 100%);clip-path:polygon(0 0,205px 0,215px 9px,100% 9px,100% 100%,0 100%)"></div>
  <div class="abs" style="right:20px;top:88px;text-align:right;color:#fff">
    <div style="font-size:12px;font-weight:700;line-height:15px">WELCOME</div>
    <div style="font-size:12px;font-weight:700;line-height:15px">TO OUR PRESENTATION</div>
    <div style="font-size:5.8px;margin-top:4px">Barcelona, August 25, 2023</div>
  </div>
  <div class="logo" style="left:21px;top:169px"><div class="mark"></div><div class="name">HARBORLINE<small>SYSTEMS</small></div></div>
</section>

<!-- 2 Outline -->
<section class="slide outline blue-bg" style="left:416px;top:37px">
  <div class="abs" style="left:94px;top:51px;font-size:9px;font-weight:300">OUTLINE</div>
  <div class="abs" style="left:94px;top:63px;width:22px;height:1px;background:#fff"></div>
  <ol class="abs" style="left:94px;top:81px;list-style:none;font-size:7.4px;font-weight:500">
    <li style="display:flex;align-items:center;gap:8px;height:21px"><span style="width:10px;height:10px;border-radius:50%;background:var(--sky);font-size:5.5px;display:flex;align-items:center;justify-content:center">1</span>Why HS</li>
    <li style="display:flex;align-items:center;gap:8px;height:21px"><span style="width:10px;height:10px;border-radius:50%;background:var(--sky);font-size:5.5px;display:flex;align-items:center;justify-content:center">2</span>ITSM Transformation &amp; Maturity</li>
    <li style="display:flex;align-items:center;gap:8px;height:21px"><span style="width:10px;height:10px;border-radius:50%;background:var(--sky);font-size:5.5px;display:flex;align-items:center;justify-content:center">3</span>Continuous Improvement Framework</li>
    <li style="display:flex;align-items:center;gap:8px;height:21px"><span style="width:10px;height:10px;border-radius:50%;background:var(--sky);font-size:5.5px;display:flex;align-items:center;justify-content:center">4</span>HS Service Towers Overview</li>
  </ol>
</section>

<!-- 3 Key facts -->
<section class="slide facts blue-bg" style="left:794px;top:37px">
  <svg class="abs" style="left:0;top:0" width="366" height="206" viewBox="0 0 366 206">
    <g fill="#3ab0ea" stroke="#fff" stroke-width="1.2">
      <circle cx="70" cy="62" r="15"/><circle cx="189" cy="62" r="15"/><circle cx="298" cy="62" r="15"/><circle cx="189" cy="139" r="15"/>
    </g>
    <g fill="none" stroke="#fff" stroke-width="1">
      <circle cx="70" cy="62" r="5"/><circle cx="70" cy="62" r="2"/>
      <rect x="182" y="55" width="6" height="5"/><rect x="191" y="55" width="6" height="5"/><rect x="186" y="64" width="6" height="5"/>
      <path d="M290 63l5-4 4 3 5-4 4 4M292 64l6 4 6-4"/>
      <rect x="181" y="134" width="16" height="11" rx="1"/><path d="M186 134v-3h6v3M181 139h16"/>
    </g>
  </svg>
  <div class="abs" style="left:20px;top:82px;width:100px;text-align:center;font-size:6.6px;line-height:8px">25+ years of IT Management Solutions Expertise</div>
  <div class="abs" style="left:134px;top:82px;width:110px;text-align:center;font-size:6.6px;line-height:8px">More than 80,000 devices under management Globally</div>
  <div class="abs" style="left:248px;top:82px;width:100px;text-align:center;font-size:6.6px;line-height:8px">Partner to top-tier enterprise and mid-market companies</div>
  <div class="abs" style="left:0;top:159px;width:366px;text-align:center;font-size:6.6px;line-height:8.8px">Serving diverse industries including :<br>Non-Profit &nbsp;I&nbsp; Transportation &amp; Logistics &nbsp;I&nbsp; Financial &amp; Banking<br>Insurance &nbsp;I&nbsp; Healthcare &nbsp;I&nbsp; Manufacturing &nbsp;I&nbsp; Real Estate &nbsp;I&nbsp; And More</div>
</section>

<!-- 4 Our services -->
<section class="slide services" style="left:35px;top:258px">
  <div class="photo blue-bg" role="img" aria-label="Hands typing on a laptop with data overlays in blue" style="left:0;top:0;width:366px;height:123px"></div>
  <div class="abs" style="left:30px;top:26px;color:#fff;font-size:9px;font-weight:300">OUR SERVICES</div>
  <div class="abs" style="left:30px;top:41px;width:20px;height:1px;background:#fff"></div>
  <p class="abs" style="left:30px;top:59px;width:265px;color:#fff;font-size:4.7px;line-height:10.6px">Lorem ipsum dolor sit amet, consectetur adipisicing elit, sed do eiusmod tempor incididunt ut labore et dolore magna aliqua. , quis nostrud exercitation ullamco laboris nisi ut aliquip ex ea commodo consequat. Duis aute irure dolor in reprehenderit</p>
  <svg class="abs" style="left:0;top:0" width="366" height="206" viewBox="0 0 366 206">
    <g fill="#3ab0ea">
      <polygon points="56,100 73,110 73,130 56,140 39,130 39,110"/>
      <polygon points="143,100 160,110 160,130 143,140 126,130 126,110"/>
      <polygon points="226,100 243,110 243,130 226,140 209,130 209,110"/>
      <polygon points="315,100 332,110 332,130 315,140 298,130 298,110"/>
    </g>
    <g fill="none" stroke="#fff" stroke-width="1">
      <rect x="50" y="110" width="12" height="8"/><circle cx="51" cy="126" r="3"/><circle cx="61" cy="126" r="3"/>
      <rect x="134" y="115" width="18" height="12" rx="1"/><path d="M139 115v-3h8v3M134 120h18"/>
      <circle cx="226" cy="115" r="3"/><path d="M217 130l4-9 5 6 5-6 4 9"/>
      <circle cx="315" cy="117" r="5"/><circle cx="315" cy="117" r="2"/><rect x="305" y="124" width="7" height="5"/><rect x="318" y="124" width="7" height="5"/>
    </g>
  </svg>
  <div class="abs" style="left:0;top:146px;width:366px;font-size:6.8px;font-weight:500;color:var(--text)">
    <span class="abs" style="left:26px">Managed Services</span>
    <span class="abs" style="left:108px">Professional Services</span>
    <span class="abs" style="left:199px">Staffing Services</span>
    <span class="abs" style="left:279px">Procurement Services</span>
  </div>
  <div class="abs" style="left:0;bottom:0;width:366px;height:3px;background:var(--sky)"></div>
</section>

<!-- 5 NOC section divider -->
<section class="slide noc-divider" style="left:416px;top:258px">
  <div class="photo blue-bg" role="img" aria-label="Hands on a keyboard under a deep blue tint" style="left:0;top:0;width:366px;height:206px;background:linear-gradient(135deg,#163f78,#1760ad 55%,#1a72c4)"></div>
  <svg class="abs" style="left:157px;top:75px" width="40" height="40" viewBox="0 0 40 40">
    <circle cx="20" cy="20" r="19" fill="none" stroke="#fff" stroke-width="1"/>
    <g fill="none" stroke="#fff" stroke-width="1.2"><circle cx="23" cy="16" r="4"/><path d="M11 26h6l5 2 8-4M11 23h5l4 2"/><path d="M14 13v4M12 15h4"/></g>
  </svg>
  <div class="abs" style="left:0;top:124px;width:366px;text-align:center;color:#fff;font-size:10px;font-weight:500">NOC Services Overview</div>
</section>

<!-- 6 NOC services -->
<section class="slide noc-services" style="left:794px;top:258px">
  <h2 class="s-title">HS NOC Services</h2><div class="s-rule"></div>
  <div class="photo" role="img" aria-label="Close-up of an eye beside a padlock shield and digital interface graphics" style="left:23px;top:37px;width:320px;height:68px;background:linear-gradient(90deg,#9db3c4 0%,#4f6f88 30%,#1f3c58 60%,#2e5570 100%)"></div>
  <div class="abs small-h" style="left:23px;top:113px">WHAT We Do</div>
  <ul class="abs bullets" style="left:22px;top:122px;width:120px;color:var(--green)">
    <li>24x7x365 Network Operations Center</li>
    <li>Real-Time Visualization</li>
    <li>Live-Event Monitoring</li>
    <li>Fault Isolation</li>
    <li>Fully-Integrated, Closed-Loop<br>Monitoring System</li>
    <li>Knowledgebase-Driven Alert Triage</li>
  </ul>
  <div class="abs small-h" style="left:164px;top:113px">WHY HS?</div>
  <p class="abs" style="left:164px;top:123px;width:179px;font-size:5.6px;line-height:10.6px;text-align:justify">Our Network Operation Center (NOC) Services are a powerful combination of automation and expertise – a proven, fine-tuned monitoring system that eliminates distracting noise so our expert technicians can focus on triaging and resolving real alerts from knowledgebase-driven playbooks efficiently and effectively before</p>
  <div class="footer-bar"><div class="g"></div><div class="b"></div><span class="n">2</span></div>
</section>

<!-- 7 Infrastructure -->
<section class="slide infrastructure" style="left:35px;top:480px">
  <h2 class="s-title">HS Infrastructure Management</h2>
  <div class="abs" style="left:0;top:48px;width:366px;height:56px;background:var(--grey-band)"></div>
  <div class="photo" role="img" aria-label="Engineer working at a computer surrounded by glowing code" style="left:23px;top:36px;width:104px;height:69px;background:linear-gradient(135deg,#0f2e44,#1d5a6e 50%,#37303a)"></div>
  <div class="abs" style="left:142px;top:63px;width:210px;color:#fff;font-size:5.6px;line-height:10.6px"><b>WHY HS?</b><br>We are thought leaders who maintain expertise across the entire technology landscape so you always have access to a partner with the skills you need</div>
  <div class="abs small-h" style="left:142px;top:115px">WHAT We Do</div>
  <ul class="abs bullets" style="left:142px;top:121px;font-size:5.6px">
    <li style="line-height:8.6px">Technology Roadmaps and Thought Leadership</li>
    <li style="line-height:8.6px">On-premise and Cloud Server Management</li>
    <li style="line-height:8.6px">CloudDesk 365 User Environment Management</li>
    <li style="line-height:8.6px">Managed Backup and Restore Services</li>
    <li style="line-height:8.6px">Systems Management &amp; OS Patching</li>
    <li style="line-height:8.6px">Disaster Recovery &amp; Business Continuity</li>
    <li style="line-height:8.6px">Capacity Management &amp; Optimization</li>
    <li style="line-height:8.6px">Database Management</li>
  </ul>
  <div class="footer-bar"><div class="g"></div><div class="b"></div><span class="n">2</span></div>
</section>

<!-- 8 Managed network -->
<section class="slide network" style="left:418px;top:480px">
  <h2 class="s-title">HS Managed Network Services</h2>
  <div class="abs" style="left:22px;top:38px;width:66px;height:84px;background:var(--red)"></div>
  <div class="photo" role="img" aria-label="Hand holding a tablet projecting a glowing security shield" style="left:28px;top:43px;width:70px;height:84px;background:linear-gradient(160deg,#2a4d74,#0e1e33 60%,#1c6f9c)"></div>
  <div class="abs small-h" style="left:23px;top:136px">WHY HS?</div>
  <p class="abs" style="left:23px;top:145px;width:117px;font-size:5.6px;line-height:10.6px;text-align:justify">Our certified and experienced engineering talent coupled with best-in-class tools and HS management disciplines means you don't have to worry about your network. Your Net work</p>
  <div class="abs small-h" style="left:181px;top:48px">WHAT We Do</div>
  <ul class="abs bullets" style="left:181px;top:55px;width:175px">
    <li>Comprehensive Data &amp; Voice Managed Network Services</li>
    <li>24x7x365 Network Monitoring</li>
    <li>Configuration and backup management</li>
    <li>Network Assessments - Data &amp; Voice</li>
    <li>VoIP Telephony &amp; Call Center Solutions</li>
    <li>Best-Practice Recommendations</li>
    <li>Onsite and Remote Support</li>
    <li>Network Visualization</li>
    <li>Configuration &amp; Firmware Management</li>
    <li>Proactive Device Backups &amp; Change Detection</li>
    <li>Design, Procurement, Installation, Configuration,<br>Management and Monitoring</li>
  </ul>
  <div class="footer-bar"><div class="g"></div><div class="b"></div><span class="n">2</span></div>
</section>

<!-- 9 Partnership -->
<section class="slide partners" style="left:794px;top:480px">
  <h2 class="s-title">Partnership</h2><div class="s-rule"></div>
  <div class="abs" style="left:35px;top:42px;width:304px;height:138px;background:#fff;box-shadow:0 0 3px rgba(0,0,0,.15);display:grid;grid-template-columns:repeat(5,1fr);grid-template-rows:repeat(5,1fr);align-items:center;justify-items:center;font-size:7.4px;font-weight:500">
    <span style="color:#1e8ec9">Calloway</span>
    <span style="color:#c8202f">Fortvane</span>
    <span style="color:#444">Meridian Partner</span>
    <span style="color:#222">Pinecrest</span>
    <span style="color:#333">Cindral</span>
    <span style="color:#d1242c">Orrin</span>
    <span style="color:#1b6fb8">Kestrel Partner</span>
    <span style="color:#333;display:flex;align-items:center;gap:2px"><i style="width:5px;height:5px;border-radius:50%;background:#f29a1b;display:inline-block"></i>Aerolith</span>
    <span style="color:#555">Vantrel</span>
    <span style="color:#2a3f7a">Ibex Data</span>
    <span style="color:#d1242c">Crestwall</span>
    <span style="color:#111">Provane</span>
    <span style="color:#c8202f">Emberlook</span>
    <span style="color:#e0701e">Rivelle</span>
    <span style="color:#4b2f7a">Sentrive</span>
    <span style="color:#1a3e7a">Nuvara</span>
    <span style="color:#333;display:flex;align-items:center;gap:2px"><i style="width:5px;height:5px;border-radius:50%;background:#f26f21;display:inline-block"></i>Clearvault</span>
    <span style="color:#1667c0;display:flex;align-items:center;gap:2px"><i style="width:5px;height:5px;background:#1667c0;display:inline-block"></i>Netmoor</span>
    <span style="color:#1d6cb8">Delmont</span>
    <span style="color:#f27521">Bellcourt</span>
    <span style="color:#1a3e7a">Linkwell</span>
    <span style="color:#17a24f">Vireo</span>
    <span style="color:#c8202f">Talvex</span>
    <span style="color:#222">Coherra</span>
    <span style="color:#1b8ca0;display:flex;align-items:center;gap:2px"><i style="width:5px;height:5px;border-radius:50%;background:#1b8ca0;display:inline-block"></i>Rubicel</span>
  </div>
  <div class="footer-bar"><div class="g"></div><div class="b"></div><span class="n">2</span></div>
</section>

<!-- 10 Why HS -->
<section class="slide why" style="left:35px;top:701px">
  <h2 class="s-title">Why HS? Measured, Managed &amp; Mature</h2><div class="s-rule"></div>
  <ul class="abs bullets" style="left:24px;top:78px;font-size:7px;color:#111">
    <li style="font-size:7px;line-height:22.5px;padding-left:10px">Business Analytics</li>
    <li style="font-size:7px;line-height:22.5px;padding-left:10px">Trend Analysis</li>
    <li style="font-size:7px;line-height:22.5px;padding-left:10px">Continuous Improvement</li>
  </ul>
  <svg class="abs" style="left:130px;top:44px" width="215" height="144" viewBox="0 0 215 144">
    <g font-family="Roboto,Arial,sans-serif">
      <rect x="3" y="3" width="174" height="92" fill="#fff" stroke="#ddd" stroke-width=".5"/>
      <rect x="3" y="3" width="174" height="4" fill="#1c2550"/>
      <text x="80" y="6.3" font-size="3" fill="#fff">Calls</text>
      <path d="M12 40a14 14 0 0 1 28 0" fill="none" stroke="#d7d9dd" stroke-width="5"/>
      <path d="M12 40a14 14 0 0 1 18-13" fill="none" stroke="#1c2550" stroke-width="5"/>
      <text x="16" y="38" font-size="4" fill="#444">200%</text>
      <rect x="44" y="18" width="20" height="4" fill="#1c2550"/>
      <text x="45" y="21" font-size="2.6" fill="#fff">Survey Results</text>
      <text x="75" y="40" font-size="5" fill="#222">465</text>
      <text x="110" y="40" font-size="5" fill="#222">33</text>
      <text x="12" y="80" font-size="5" fill="#222">15</text>
      <g fill="#5aa0e0"><rect x="145" y="30" width="20" height="3"/><rect x="145" y="36" width="14" height="3"/><rect x="145" y="42" width="18" height="3"/></g>
      <rect x="28" y="50" width="150" height="80" fill="#fff" stroke="#ddd" stroke-width=".5"/>
      <text x="32" y="115" font-size="5" fill="#222">99.50</text>
      <g fill="#1c2550"><rect x="70" y="60" width="4" height="30"/><rect x="76" y="68" width="4" height="22"/></g>
      <rect x="85" y="58" width="125" height="82" fill="#fff" stroke="#ddd" stroke-width=".5"/>
      <g stroke="#e5e6ea" stroke-width=".5"><path d="M92 66h30M92 70h30M92 74h30M92 78h30M92 82h30M92 86h30"/></g>
      <rect x="160" y="78" width="30" height="3" fill="#1c2550"/>
      <text x="140" y="70" font-size="3" fill="#555">Resolved by Month</text>
      <circle cx="104" cy="120" r="11" fill="#c8202f"/>
      <path d="M104 120V109a11 11 0 0 1 10 6z" fill="#2a4e9a"/>
      <path d="M104 120l10-5a11 11 0 0 1-3 13z" fill="#7fb3e6"/>
      <circle cx="165" cy="120" r="11" fill="#7fb3e6"/>
      <path d="M165 120V109a11 11 0 0 0-11 9z" fill="#c8202f"/>
      <path d="M165 120l-11-2a11 11 0 0 0 6 12z" fill="#f0a0a6"/>
    </g>
  </svg>
  <div class="footer-bar"><div class="g"></div><div class="b"></div><span class="n">2</span></div>
</section>

<!-- 11 Escalation -->
<section class="slide escalation" style="left:418px;top:701px">
  <h2 class="s-title">Escalation Analysis</h2>
  <div class="abs" style="left:20px;top:37px;font-size:5.6px">Trend analysis Drives Continuous Improvement</div>
  <svg class="abs" style="left:0;top:0" width="366" height="206" viewBox="0 0 366 206">
    <g font-family="Roboto,Arial,sans-serif">
      <rect x="37" y="53" width="124" height="68" fill="#fff" stroke="#ccc" stroke-width=".5"/>
      <rect x="37" y="53" width="124" height="4" fill="#3556a8"/>
      <text x="40" y="56.2" font-size="2.6" fill="#fff">Escalation Flow</text>
      <rect x="37" y="57" width="3" height="64" fill="#3556a8"/>
      <g stroke="#3556a8" stroke-width=".5" fill="none"><path d="M40 80h121M40 100h121"/><path d="M52 74v16h20M64 90v14h20"/></g>
      <g fill="#2fae4b"><circle cx="78" cy="85" r="3"/><circle cx="100" cy="98" r="3"/><circle cx="118" cy="114" r="3"/></g>
      <rect x="38" y="125" width="120" height="64" fill="#fff" stroke="#ccc" stroke-width=".5"/>
      <text x="80" y="130" font-size="2.8" fill="#333">Top Escalations</text>
      <circle cx="80" cy="157" r="14" fill="none" stroke="#1c2a6b" stroke-width="7"/>
      <path d="M80 143a14 14 0 0 0-13 9" fill="none" stroke="#e0506a" stroke-width="7"/>
      <path d="M67 152a14 14 0 0 0 3 15" fill="none" stroke="#36ade6" stroke-width="7"/>
      <g fill="#1c2a6b"><rect x="118" y="140" width="2" height="2"/><rect x="118" y="146" width="2" height="2"/><rect x="118" y="152" width="2" height="2"/><rect x="118" y="158" width="2" height="2"/><rect x="118" y="164" width="2" height="2"/></g>
      <!-- process rings -->
      <path d="M218 19h25a27 27 0 0 1 13 50" fill="none" stroke="#36ade6" stroke-width="6"/>
      <path d="M236 70a25 25 0 1 0 0 24" fill="none" stroke="#1c3a6b" stroke-width="6"/>
      <path d="M238 106a25 25 0 1 1 20 36" fill="none" stroke="#a7a9ac" stroke-width="6"/>
      <path d="M238 142a25 25 0 1 0 0 25" fill="none" stroke="#c41f2e" stroke-width="6"/>
      <circle cx="256" cy="46" r="16" fill="#36ade6"/>
      <circle cx="221" cy="82" r="16" fill="#1c3a6b"/>
      <circle cx="256" cy="118" r="16" fill="#8f9194"/>
      <circle cx="221" cy="154" r="16" fill="#c41f2e"/>
      <g font-size="5.6" font-weight="700" fill="#fff" text-anchor="middle">
        <text x="256" y="48">Analysis</text>
        <text x="221" y="80">Under</text><text x="221" y="87">standing</text>
        <text x="256" y="120">Action</text>
        <text x="221" y="156">Results</text>
      </g>
      <g font-size="4.6" fill="#36ade6"><text x="298" y="45">• Why are we escalating</text><text x="298" y="53">• When do we escalate</text></g>
      <g font-size="4.6" fill="#1c3a6b"><text x="276" y="80">• Lack of Knowledge</text><text x="276" y="88">• Lack of Access</text></g>
      <g font-size="4.6" fill="#8f9194"><text x="290" y="104">• Drive process</text><text x="296" y="112">improvements</text><text x="290" y="120">• Build knowledge</text><text x="290" y="128">• Ensure the right level</text><text x="296" y="136">of access</text></g>
      <g font-size="4.6" fill="#c41f2e"><text x="245" y="157">• Increased first call resolution</text><text x="245" y="165">• Increased quality</text><text x="245" y="173">• Increased speed of resolution</text></g>
    </g>
  </svg>
  <div class="footer-bar"><div class="g"></div><div class="b"></div><span class="n">2</span></div>
</section>

<!-- 12 Thank you -->
<section class="slide thanks" style="left:794px;top:703px">
  <div class="logo" style="left:20px;top:14px"><div class="mark"></div><div class="name">HARBORLINE<small>SYSTEMS</small></div></div>
  <div class="abs blue-bg" style="left:0;top:56px;width:366px;height:150px;clip-path:polygon(0 0,205px 0,215px 9px,100% 9px,100% 100%,0 100%);background:linear-gradient(135deg,#163f78,#1a5aa6 60%,#1c6fc0)"></div>
  <div class="abs" style="left:260px;top:104px;color:#fff;font-size:12px;font-weight:300">THANK YOU</div>
  <div class="abs" style="left:260px;top:141px;color:#fff;font-size:5.4px;line-height:14px">
    <div style="display:flex;align-items:center;gap:4px"><i style="width:7px;height:7px;border:1px solid #fff;border-radius:50%;display:inline-block"></i>hello@harborline-sys.net</div>
    <div style="display:flex;align-items:center;gap:4px"><i style="width:7px;height:7px;border:1px solid #fff;border-radius:50%;display:inline-block"></i>www.harborline-sys.net</div>
    <div style="display:flex;gap:3px;margin-top:1px"><i style="width:8px;height:8px;background:#fff;display:inline-block"></i><i style="width:8px;height:8px;background:#fff;display:inline-block"></i><i style="width:8px;height:8px;background:#fff;display:inline-block"></i></div>
  </div>
</section>

</body>
</html>
```